VR Autohaus Website

We currently have a great webpage www.vrwagen.ch. We realise we need a new look and have new features added:

New website: Design a new professional website with a "WOW" factor / state of the art user-friendly layout for the car industry. Keep the Corporate Identity (colors) of EQ  Motors and restructure the current menus and webdesign to categorize into products and services. some of the subpages create new, others include our existing ones.

 

Products:

1. New Cars (subpage just include existing one)

2. Used Cars (subpage just include existing one)

3. Car parts (subpage shop just include existing one)

 

Services:

1. Car wrapping/ folierung (create new subpage leveraging on existing one)

2. car rental (create new subpage and include existing car rental portal)

3. Fahrzeugaufbereitung/ car washing (create new subpage)

4. Import / export services (create new subpage)

5. Mechanics & installation and maintenance services (create new subpage)

6. bump fixing (create new subpage)

 

Structural / layout guidance for design, pls see enclosed. Design-wise, pls show us better than this.

 

Target Market(s)

Car Owners

Industry/Entity Type

Automotive

Number of Pages Required

4 page

Requirements
Must have
• Theme colours : red, black & white
• With codings.
• We would like to see how each sub links look like as whole websites.
• We can build up for further discussion on development with the winner.
Nice to have
• An eye catching promotions box, using some sort of "Flash"

```html
<!DOCTYPE html>
<html lang="en">
<head>
<meta charset="utf-8">
<title>VR Autohaus</title>
<link href="https://fonts.googleapis.com/css2?family=Open+Sans:wght@400;600;700;800&family=Roboto+Condensed:wght@400;700&display=swap" rel="stylesheet">
<style>
:root{
  --red:#d6201f;
  --red-dark:#b01616;
  --black:#1b1b1b;
  --charcoal:#2b2b2b;
  --footer:#262626;
  --footer-deep:#1a1a1a;
  --grey:#e9e9e9;
  --text:#444;
  --muted:#888;
  --white:#fff;
}
*{box-sizing:border-box;margin:0;padding:0}
html,body{width:683px;height:1200px;overflow:hidden}
body{font-family:"Open Sans",Arial,sans-serif;color:var(--text);background:var(--white);font-size:7px;line-height:1.35;display:flex;flex-direction:column}
.wrap{width:640px;margin:0 auto;position:relative}
.btn{display:inline-block;background:var(--red);color:var(--white);font-family:"Roboto Condensed",Arial,sans-serif;font-weight:700;font-size:7px;padding:4px 9px;text-transform:uppercase;letter-spacing:.3px}
.btn.dark{background:var(--black)}

/* header */
.site-header{height:64px;flex:none;position:relative}
.brand{position:absolute;left:21px;top:10px;display:flex;align-items:center;gap:6px}
.brand-dot{width:38px;height:38px;border-radius:50%;background:var(--red)}
.brand-name{font-weight:800;font-size:19px;color:var(--black);letter-spacing:-.3px}
.brand-tag{position:absolute;left:65px;top:40px;font-size:5px;color:var(--muted)}
.topline{position:absolute;right:21px;top:8px;display:flex;gap:14px;font-size:6.5px;color:var(--muted)}
.topline b{color:var(--black)}
.main-nav{position:absolute;right:21px;top:30px;display:flex;gap:2px}
.main-nav a{background:var(--black);color:var(--white);font-family:"Roboto Condensed",Arial,sans-serif;font-weight:700;font-size:7px;padding:8px 9px;text-decoration:none}
.main-nav a.active{background:var(--red)}

/* hero */
.hero{height:212px;flex:none;position:relative;background:linear-gradient(180deg,#f4f4f4 0%,#cfd2d4 55%,#9ea3a6 100%);border-top:3px solid var(--red)}
.hero-visual{position:absolute;left:40px;top:18px;width:420px;height:180px;border-radius:50% 50% 30% 30%/60% 60% 25% 25%;background:radial-gradient(ellipse at 50% 55%,#8d9398 0%,#b8bcbf 45%,rgba(200,203,206,0) 72%)}
.hero-caption{position:absolute;right:70px;top:58px;width:160px}
.hero-caption p{background:rgba(30,30,30,.78);color:var(--white);font-size:8px;line-height:1.4;padding:8px 10px}
.hero-caption .actions{margin-top:4px;display:flex;gap:3px}
.hero-arrow{position:absolute;top:90px;width:16px;height:30px;background:var(--red);display:flex;align-items:center;justify-content:center}
.hero-arrow.prev{left:0}.hero-arrow.next{right:0}

/* product cards */
.products{display:flex;gap:14px;padding:16px 0 0}
.product{flex:1;height:150px;border:1px solid #ddd;background:var(--white);position:relative;padding:24px 8px 8px;box-shadow:0 2px 3px rgba(0,0,0,.08)}
.product-tag{position:absolute;top:-1px;left:50%;transform:translateX(-50%);background:var(--red);color:var(--white);font-family:"Roboto Condensed",Arial,sans-serif;font-weight:700;font-size:7px;padding:3px 10px;text-transform:uppercase}
.product p{font-size:7px;width:70px}
.new .photo{position:absolute;right:8px;top:70px;width:120px;height:66px;background:radial-gradient(ellipse at 50% 60%,#2a2a2a 0%,#6a6a6a 50%,#fff 75%)}
.new .flag{position:absolute;left:90px;top:30px;width:30px;height:30px;border-radius:50%;background:var(--red);color:var(--white);font-size:5.5px;font-weight:700;text-align:center;padding-top:6px;line-height:1.25}
.used .thumb{position:absolute;left:8px;top:26px;width:60px;height:40px;background:linear-gradient(135deg,#d9dadb,#8b8f92)}
.used .spec{position:absolute;left:74px;top:26px;font-size:6px;color:var(--muted)}
.used .spec b{display:block;color:var(--black);font-size:7.5px}
.used .price{position:absolute;left:8px;top:80px;font-weight:700;font-size:12px;color:var(--black)}
.used .note{position:absolute;left:8px;bottom:10px;font-size:6px;width:180px}
.parts .cart{position:absolute;right:30px;top:36px}
.parts .shop{position:absolute;right:22px;top:96px;font-weight:700;font-size:9px;color:var(--black)}
.parts p{margin-top:10px}

/* partner badges */
.partners{display:flex;justify-content:space-between;padding:16px 8px 10px}
.partners span{width:42px;height:14px;border-radius:7px;background:#d8d8d8}

/* services */
.services{display:flex;gap:8px;padding-top:6px}
.service{flex:1}
.service h3{font-family:"Roboto Condensed",Arial,sans-serif;font-weight:700;color:var(--red);font-size:7.5px;height:22px;text-transform:uppercase;line-height:1.2;border-bottom:1px solid #ddd;padding-bottom:2px}
.service .photo{height:92px;margin:7px 0}
.service h4{font-size:6.5px;color:var(--black);font-weight:700;text-transform:uppercase}
.service p{font-size:6px;color:var(--muted);height:34px}
.wrap-img{background:linear-gradient(135deg,#7fbbe3,#1c6fb4)}
.rent-img{background:linear-gradient(135deg,#b7e36d,#3b8f2a)}
.wash-img{background:linear-gradient(135deg,#e0e4e8,#8ea1b3)}
.import-img{background:linear-gradient(135deg,#5c6a78,#1f2a35)}
.mech-img{background:linear-gradient(135deg,#d9c6a6,#6d5844)}

/* promos */
.promos{display:flex;gap:8px;padding-top:16px}
.promo{flex:1;height:106px;position:relative}
.promo.care{background:linear-gradient(135deg,#f3f3f3,#b5bcc4 70%,#7d8790)}
.promo.seat{background:linear-gradient(135deg,#ffd23f,#ef8a1f 60%,#d6201f)}
.promo.month{background:var(--charcoal);color:var(--white);padding:18px 12px}
.promo.month h2{font-size:17px;font-weight:600;line-height:1.15;margin-bottom:8px}

/* testimonials */
.testimonials{flex:none;margin-top:10px;background:#f2f2f2;padding:12px 0;height:164px}
.testimonials .wrap{display:flex;gap:16px}
.quote{flex:1}
.quote h2{font-family:"Roboto Condensed",Arial,sans-serif;color:var(--red);font-size:10px;text-transform:uppercase;margin-bottom:6px}
.quote p{font-size:6.5px;background:var(--white);padding:8px;border:1px solid #ddd}
.quote .who{margin-top:8px;font-weight:700;color:var(--black);font-size:7px}
.testi-photo{width:300px;height:140px;background:linear-gradient(160deg,#4a4a4a,#1d1d1d 60%,#7a1414)}

/* footer */
.site-footer{flex:1;background:var(--footer);color:#bbb;padding-top:16px}
.site-footer .wrap{display:flex;gap:16px}
.col h5{color:var(--white);font-family:"Roboto Condensed",Arial,sans-serif;font-size:8px;text-transform:uppercase;margin-bottom:8px}
.col p,.col li{font-size:6.5px;list-style:none;margin-bottom:5px}
.col.hours{width:110px}.col.contact{width:140px}.col.tweets{width:170px}.col.news{flex:1}
.contact li{display:flex;gap:5px;align-items:flex-start}
.tweets li{display:flex;gap:5px}
.tweets li span{color:var(--red)}
.news input{width:100%;height:18px;border:0;background:var(--white);font-size:6.5px;padding:0 6px;margin:6px 0}
.bottom-bar{flex:none;background:var(--footer-deep);height:50px;position:relative}
.bottom-bar .brand-name{color:var(--white);font-size:15px}
.bottom-bar .brand{top:12px}
.bottom-bar .brand-dot{width:26px;height:26px}
.legal{position:absolute;right:21px;top:12px;text-align:right;font-size:6px;color:#999}
.social{display:flex;gap:4px;justify-content:flex-end;margin-bottom:5px}
.social span{width:11px;height:11px;border-radius:50%;background:#555}
</style>
</head>
<body>

<header class="site-header">
  <div class="brand"><span class="brand-dot"></span><span class="brand-name">VR Wagen AG</span></div>
  <div class="brand-tag">Autohandel · Service · Vermietung</div>
  <div class="topline"><span>FREE CALL: <b>+41 44 555 01 20</b></span><span>English ▾</span></div>
  <nav class="main-nav">
    <a class="active" href="#">HOME</a><a href="#">PRODUCTS</a><a href="#">SERVICES</a><a href="#">CAR WRAPPING</a><a href="#">ENQUIRY</a><a href="#">ABOUT US</a><a href="#">STORE</a>
  </nav>
</header>

<section class="hero">
  <div class="hero-visual" role="img" aria-label="Silver electric sports coupe with open door on a light studio floor"></div>
  <div class="hero-caption">
    <p>Lorem Ipsum is simply dummy text of the printing and typesetting industry.</p>
    <div class="actions"><span class="btn">Find more</span><span class="btn dark">Book now</span></div>
  </div>
  <div class="hero-arrow prev"><svg width="8" height="12"><path d="M7 1 2 6l5 5" stroke="#fff" stroke-width="2" fill="none"/></svg></div>
  <div class="hero-arrow next"><svg width="8" height="12"><path d="M1 1l5 5-5 5" stroke="#fff" stroke-width="2" fill="none"/></svg></div>
</section>

<main class="wrap">
  <section class="products">
    <article class="product new">
      <span class="product-tag">New cars</span>
      <p>Lorem Ipsum is simply dummy text of the printing and typesetting.</p>
      <span class="flag">ab<br>CHF<br>29'900</span>
      <div class="photo" role="img" aria-label="Black luxury saloon, front three-quarter view"></div>
    </article>
    <article class="product used">
      <span class="product-tag">Used cars</span>
      <div class="thumb" role="img" aria-label="Silver compact SUV"></div>
      <div class="spec"><b>Sportline Crossover</b>Inverkehrsetzung 2014<br>Kilometer 12'000<br>Benzin, Automat</div>
      <div class="price">CHF 95'000.00</div>
      <p class="note">Lorem Ipsum is simply dummy text of the printing and typesetting.</p>
    </article>
    <article class="product parts">
      <span class="product-tag">Car parts</span>
      <p>Lorem Ipsum is simply dummy text of the printing and typesetting.</p>
      <svg class="cart" width="56" height="52" viewBox="0 0 56 52"><path d="M2 6h9l7 28h28l6-20H15" fill="none" stroke="#333" stroke-width="4" stroke-linejoin="round"/><circle cx="22" cy="44" r="5" fill="#333"/><circle cx="42" cy="44" r="5" fill="#333"/></svg>
      <span class="shop">ONLINE SHOP</span>
    </article>
  </section>

  <div class="partners" aria-label="Partner brands">
    <span></span><span></span><span></span><span></span><span></span><span></span><span></span><span></span><span></span><span></span><span></span>
  </div>

  <section class="services">
    <article class="service">
      <h3>Car wrapping</h3>
      <div class="photo wrap-img" role="img" aria-label="Car with blue vinyl wrap"></div>
      <h4>Neuwagen auf Bestellung</h4>
      <p>Lorem ipsum dummy text of the printing industry.</p>
      <span class="btn">Send inquiry</span>
    </article>
    <article class="service">
      <h3>Car rental</h3>
      <div class="photo rent-img" role="img" aria-label="Green compact rental car"></div>
      <h4>Neuwagen auf Bestellung</h4>
      <p>Lorem ipsum dummy text of the printing industry.</p>
      <span class="btn">View more</span>
    </article>
    <article class="service">
      <h3>Car washing</h3>
      <div class="photo wash-img" role="img" aria-label="Car being washed with foam"></div>
      <h4>Your benefits</h4>
      <p>Lorem ipsum dummy text of the printing industry.</p>
      <span class="btn">Book now</span>
    </article>
    <article class="service">
      <h3>Import / export administration</h3>
      <div class="photo import-img" role="img" aria-label="Cars lined up at a shipping port"></div>
      <h4>Car wrapping folierung</h4>
      <p>Lorem ipsum dummy text of the printing industry.</p>
      <span class="btn">Book now</span>
    </article>
    <article class="service">
      <h3>Car mechanics &amp; maintenance</h3>
      <div class="photo mech-img" role="img" aria-label="Mechanic servicing an engine"></div>
      <h4>Car wrapping folierung</h4>
      <p>Lorem ipsum dummy text of the printing industry.</p>
      <span class="btn">Book now</span>
    </article>
  </section>

  <section class="promos">
    <div class="promo care" role="img" aria-label="Premium car care banner with polished bodywork"></div>
    <div class="promo seat" role="img" aria-label="Offer banner: get a free Roadline car seat, with child seat product"></div>
    <div class="promo month">
      <h2>Promotion of<br>the month</h2>
      <span class="btn">Learn more</span>
    </div>
  </section>
</main>

<section class="testimonials">
  <div class="wrap">
    <div class="quote">
      <h2>Testimonials</h2>
      <p>“Contrary to popular belief, Lorem Ipsum is not simply random text. It has roots in a piece of classical Latin literature from 45 BC, making it over 2000 years old. A professor at a college looked up one of the more obscure Latin words and went through the cites of the word in classical literature.”</p>
      <div class="who">Martin Keller, ZH</div>
    </div>
    <div class="testi-photo" role="img" aria-label="Dark sports car at night with red light streaks"></div>
  </div>
</section>

<footer class="site-footer">
  <div class="wrap">
    <div class="col hours">
      <h5>Office timing</h5>
      <ul><li>Mo: 08.00 - 18.30</li><li>Di: 08.00 - 18.30</li><li>Mi: 08.00 - 18.30</li><li>Do: 08.00 - 18.30</li><li>Fr: 08.00 - 18.30</li><li>Sa: 09.00 - 16.00</li></ul>
    </div>
    <div class="col contact">
      <h5>Contact us</h5>
      <ul>
        <li><svg width="8" height="8" viewBox="0 0 8 8"><path d="M1 1h2l1 2-1 1a5 5 0 0 0 2 2l1-1 2 1v2C4 8 0 4 1 1z" fill="#d6201f"/></svg>+41 44 555 01 20</li>
        <li><svg width="8" height="8" viewBox="0 0 8 8"><path d="M4 0a3 3 0 0 0-3 3c0 2 3 5 3 5s3-3 3-5a3 3 0 0 0-3-3z" fill="#d6201f"/></svg>Werkstrasse 14<br>8050 Zürich</li>
        <li><svg width="8" height="8" viewBox="0 0 8 8"><rect x="0" y="1" width="8" height="6" fill="#d6201f"/></svg>info@vrwagen.ch</li>
      </ul>
    </div>
    <div class="col tweets">
      <h5>Latest tweets</h5>
      <ul>
        <li><span>›</span>Lorem Ipsum is simply dummy text of the printing and typesetting industry.</li>
        <li><span>›</span>Lorem Ipsum is simply dummy text of the printing and typesetting industry.</li>
        <li><span>›</span>Lorem Ipsum is simply dummy text of the printing and typesetting industry.</li>
      </ul>
    </div>
    <div class="col news">
      <h5>Newsletter</h5>
      <p>Lorem Ipsum is simply dummy text of the printing and typesetting industry.</p>
      <input type="text" value="E-mail address" aria-label="E-mail address">
      <span class="btn">Subscribe</span>
    </div>
  </div>
</footer>

<div class="bottom-bar">
  <div class="brand"><span class="brand-dot"></span><span class="brand-name">VR Wagen AG</span></div>
  <div class="legal">
    <div class="social"><span></span><span></span><span></span><span></span></div>
    © VR Wagen AG | Impressum | Sitemap | Neuwagen | Occasionen | Kontakt
  </div>
</div>

</body>
</html>
```